FRONT BUS CARD:

We were maybe thinking to have the text in a "common seal" which is an oval shape. Or CROWN VAULT underlined, then AUSTRALIA underneath...

Picture to have in the seal, or next to the words if seal not used: Gold Bars (3 of them), or scales of justice..

LOGO and pic and font to be in shiny gold.
We want 1 black background design and 1 white background design.

CROWN VAULT TRADERS

```html
<!DOCTYPE html>
<html lang="en">
<head>
<meta charset="utf-8">
<title>Crown Vault Traders – Business Cards</title>
<link rel="stylesheet" href="https://fonts.googleapis.com/css2?family=EB+Garamond:wght@400;600&display=swap">
<style>
  :root {
    --backdrop: #8a7a66;
    --card-black: #050505;
    --gold: #e2b13c;
    --ink-light: #f2f2f2;
    --ghost: #151515;
  }
  * { margin: 0; padding: 0; box-sizing: border-box; }
  html, body { width: 1200px; height: 900px; overflow: hidden; }
  body {
    background: var(--backdrop);
    font-family: "EB Garamond", Georgia, serif;
    position: relative;
  }
  .card {
    position: absolute;
    left: 280px;
    width: 640px;
    height: 366px;
    background: var(--card-black);
    overflow: hidden;
    box-shadow: 0 10px 24px rgba(0,0,0,0.35);
  }
  .card--front { top: 66px; }
  .card--back { top: 468px; }

  .brand {
    display: flex;
    align-items: center;
    gap: 12px;
    color: var(--gold);
    font-weight: 600;
    text-transform: uppercase;
    line-height: 1.05;
  }
  .brand__dot {
    border-radius: 50%;
    background: var(--gold);
    flex: none;
  }
  .card--front .brand {
    position: absolute;
    left: 50%;
    top: 50%;
    transform: translate(-50%, -50%);
    font-size: 40px;
    letter-spacing: 3px;
    white-space: nowrap;
  }
  .card--front .brand__dot { width: 22px; height: 22px; }

  .card--back .brand {
    position: absolute;
    left: 54px;
    top: 44px;
    font-size: 20px;
    letter-spacing: 1.5px;
  }
  .card--back .brand__dot { width: 12px; height: 12px; }

  .brand-ghost {
    position: absolute;
    right: -30px;
    top: 90px;
    font-size: 96px;
    font-weight: 600;
    line-height: 0.95;
    color: var(--ghost);
    text-transform: uppercase;
    text-align: right;
    white-space: nowrap;
  }

  .person {
    position: absolute;
    left: 54px;
    top: 158px;
  }
  .person__name {
    color: var(--gold);
    font-size: 27px;
    font-weight: 400;
    line-height: 1.1;
  }
  .person__role {
    color: var(--ink-light);
    font-size: 16px;
    margin-top: 2px;
  }
  .contact {
    position: absolute;
    left: 54px;
    top: 256px;
    list-style: none;
    color: var(--ink-light);
    font-size: 15.5px;
    line-height: 1.45;
  }
  .contact__label { color: var(--gold); margin-right: 4px; }
</style>
</head>
<body>
  <section class="card card--front" aria-label="Business card front">
    <div class="brand">
      <span class="brand__dot"></span>
      <span class="brand__name">Crown Vault<br>Traders</span>
    </div>
  </section>

  <section class="card card--back" aria-label="Business card back">
    <div class="brand-ghost" aria-hidden="true">Crown<br>Vault</div>
    <div class="brand">
      <span class="brand__dot"></span>
      <span class="brand__name">Crown Vault<br>Traders</span>
    </div>
    <div class="person">
      <p class="person__name">Marcus Ellery</p>
      <p class="person__role">Owner/Founder</p>
    </div>
    <ul class="contact">
      <li><span class="contact__label">p:</span>123-418-7702</li>
      <li><span class="contact__label">e:</span>marcus@crownvaulttraders.com</li>
      <li><span class="contact__label">w:</span>www.crownvaulttraders.com</li>
    </ul>
  </section>
</body>
</html>
```